Trade show backdrop

I have a rough layout of what I need for my 10ft.x7.6ft backdrop, the printer said they can't use my artwork as it is too small. I need someone to design it to send to printer in proper formate. It need to be done by next week

```html
<!DOCTYPE html>
<html lang="en">
<head>
<meta charset="utf-8">
<title>Regency Fabric Care – Tradeshow Backdrop</title>
<link rel="stylesheet" href="https://fonts.googleapis.com/css2?family=Archivo+Black&family=Arimo:wght@400;700&family=Jost:wght@400;500&family=Noto+Serif:ital,wght@0,400;0,700;1,700&display=swap">
<style>
  :root {
    --navy: #0b1628;
    --gold: #f5a31a;
    --sand: #d8cbb8;
    --paper: #f0e4da;
    --white: #ffffff;
    --ink: #0a0a0a;
  }
  * { box-sizing: border-box; margin: 0; padding: 0; }
  html, body { width: 1200px; height: 675px; overflow: hidden; background: var(--paper); }
  .canvas { position: relative; width: 1200px; height: 675px; background: var(--paper); font-family: "Arimo", sans-serif; }
  .abs { position: absolute; }

  .backdrop { position: absolute; left: 22px; top: 17px; width: 843px; height: 641px; background: var(--navy); }
  .rule-v { position: absolute; width: 2px; background: var(--gold); }
  .rule-h { position: absolute; height: 2px; background: var(--gold); }

  /* specialist column */
  .questions { left: 22px; top: 52px; width: 190px; text-align: center; font: 700 20px/1 "Arimo", sans-serif; color: var(--gold); }
  .ask { left: 22px; top: 78px; width: 190px; text-align: center; font: 400 16px/1 "Arimo", sans-serif; color: var(--white); }
  .portrait { left: 54px; top: 114px; width: 131px; height: 146px; border: 2px solid var(--gold); background: linear-gradient(160deg, #b9bfa6 0%, #8d8f7c 55%, #2a2c33 100%); }
  .specialist-name { left: 22px; top: 266px; width: 195px; text-align: center; font: 700 21px/1 "Noto Serif", serif; color: var(--white); }
  .service { position: absolute; left: 55px; display: flex; align-items: flex-start; gap: 10px; color: var(--white); font: 400 10.5px/13px "Arimo", sans-serif; }
  .service svg { flex: none; width: 28px; height: 28px; }
  .service span { padding-top: 1px; }

  /* centre column */
  .brand { left: 212px; top: 17px; width: 457px; height: 194px; display: flex; flex-direction: column; align-items: center; justify-content: center; color: var(--white); font-family: "Noto Serif", serif; font-weight: 700; }
  .brand-main { font-size: 66px; line-height: 1; letter-spacing: -1px; }
  .brand-sub { font-size: 30px; line-height: 1.2; margin-top: 6px; }
  .photo { top: 212px; height: 172px; }
  .photo-cleaning { left: 212px; width: 222px; background: linear-gradient(180deg, #8f8a84 0%, #6e655c 45%, #5a2a1e 70%, #8a4b1f 100%); }
  .photo-living { left: 444px; width: 225px; background: linear-gradient(180deg, #cdc2b5 0%, #b9ac9c 50%, #e6dfd6 70%, #3b3a3c 100%); }
  .protection { left: 224px; top: 404px; font: 400 16.5px/20px "Noto Serif", serif; color: var(--white); }
  .partner { left: 500px; top: 408px; width: 160px; display: flex; align-items: center; justify-content: center; gap: 6px; font: 700 15px/1 "Arimo", sans-serif; color: var(--white); }
  .partner i { width: 10px; height: 10px; border-radius: 50%; background: var(--gold); display: block; }
  .contact-box { left: 212px; top: 469px; width: 457px; height: 103px; background: var(--sand); }
  .tagline { left: 212px; top: 480px; width: 457px; text-align: center; font: 700 26px/1 "Noto Serif", serif; color: var(--navy); }
  .phone { left: 248px; top: 529px; font: 400 19px/1 "Arimo", sans-serif; color: var(--navy); }
  .contact-divider { left: 442px; top: 524px; width: 2px; height: 32px; background: var(--gold); }
  .website { left: 494px; top: 529px; font: 400 19px/1 "Arimo", sans-serif; color: var(--navy); }
  .qr-slot { left: 586px; top: 518px; width: 39px; height: 39px; background: #f1f1f1; }
  .history { left: 212px; top: 586px; width: 457px; text-align: center; font: 700 18.5px/24px "Noto Serif", serif; color: var(--white); }

  /* values & credentials column */
  .mission { left: 672px; top: 50px; width: 193px; text-align: center; font: italic 700 23px/24px "Noto Serif", serif; color: var(--gold); }
  .values { left: 700px; top: 128px; list-style: none; color: var(--white); font: 400 15px/27.5px "Arimo", sans-serif; }
  .values li { display: flex; align-items: center; gap: 12px; }
  .values li::before { content: ""; width: 6px; height: 6px; border-radius: 50%; background: var(--gold); }
  .credentials-title { left: 672px; top: 267px; width: 193px; text-align: center; font: italic 700 22px/1 "Noto Serif", serif; color: var(--gold); }
  .credential { position: absolute; left: 687px; display: flex; gap: 7px; color: var(--white); font: 400 13px/16.5px "Arimo", sans-serif; }
  .credential svg { flex: none; width: 26px; height: 26px; margin-top: 2px; }
  .certificate-frame { left: 682px; top: 490px; width: 169px; height: 135px; border: 2px solid var(--gold); }
  .certificate { left: 689px; top: 499px; width: 154px; height: 119px; background: linear-gradient(135deg, #efe6cf 0%, #d9cba6 100%); border: 3px solid #8a7a5a; }

  /* spec sheet */
  .spec-title { left: 884px; top: 42px; font: 400 43px/41px "Archivo Black", sans-serif; color: var(--ink); }
  .spec-label { position: absolute; left: 884px; font: 500 21px/1 "Jost", sans-serif; color: var(--ink); }
  .spec-value { position: absolute; left: 883px; font: 500 41px/1 "Jost", sans-serif; color: var(--ink); }
  .spec-note { position: absolute; left: 884px; font: 500 18.5px/22px "Jost", sans-serif; color: var(--ink); }
  .swatch { position: absolute; top: 624px; width: 23px; height: 23px; border-radius: 50%; }
</style>
</head>
<body>
<div class="canvas">

  <div class="backdrop"></div>
  <div class="rule-v" style="left:211px; top:17px; height:641px;"></div>
  <div class="rule-v" style="left:669px; top:17px; height:641px;"></div>
  <div class="rule-h" style="left:212px; top:210px; width:457px;"></div>
  <div class="rule-v" style="left:434px; top:211px; height:174px; width:10px; background:var(--navy); border-left:2px solid var(--gold); border-right:2px solid var(--gold);"></div>
  <div class="rule-h" style="left:212px; top:384px; width:457px;"></div>
  <div class="rule-h" style="left:212px; top:467px; width:457px;"></div>
  <div class="rule-h" style="left:212px; top:573px; width:457px;"></div>

  <!-- specialist column -->
  <div class="abs questions">QUESTIONS?</div>
  <div class="abs ask">Ask the Specialist</div>
  <div class="abs portrait" role="img" aria-label="Portrait photo of the rug specialist"></div>
  <div class="abs specialist-name">Walter Hensley</div>

  <div class="service" style="top:309px;">
    <svg viewBox="0 0 28 28"><circle cx="14" cy="14" r="12.5" fill="none" stroke="var(--gold)" stroke-width="1.5"/><rect x="9" y="8" width="10" height="12" fill="none" stroke="var(--gold)" stroke-width="1.4"/><path d="M9 8 19 20M19 8 9 20" stroke="var(--gold)" stroke-width="1"/></svg>
    <span>Oriental rug and<br>area rug cleaning</span>
  </div>
  <div class="service" style="top:354px;">
    <svg viewBox="0 0 28 28"><circle cx="14" cy="14" r="12.5" fill="none" stroke="var(--gold)" stroke-width="1.5"/><ellipse cx="14" cy="17" rx="4" ry="3.2" fill="var(--gold)"/><circle cx="9" cy="12" r="1.8" fill="var(--gold)"/><circle cx="12" cy="9" r="1.8" fill="var(--gold)"/><circle cx="16" cy="9" r="1.8" fill="var(--gold)"/><circle cx="19" cy="12" r="1.8" fill="var(--gold)"/></svg>
    <span>Pet standard Odor<br>removal 100%<br>Guaranteed</span>
  </div>
  <div class="service" style="top:402px;">
    <svg viewBox="0 0 28 28"><circle cx="14" cy="14" r="12.5" fill="none" stroke="var(--gold)" stroke-width="1.5"/><rect x="13" y="8" width="7" height="12" rx="1" fill="none" stroke="var(--gold)" stroke-width="1.4"/><path d="M8 8v12M6 11h4M6 17h4" stroke="var(--gold)" stroke-width="1.4"/></svg>
    <span>Rug<br>Repairs</span>
  </div>
  <div class="service" style="top:445px;">
    <svg viewBox="0 0 28 28"><circle cx="14" cy="14" r="12.5" fill="none" stroke="var(--gold)" stroke-width="1.5"/><circle cx="12.5" cy="12.5" r="4.5" fill="none" stroke="var(--gold)" stroke-width="1.6"/><path d="M16 16l4.5 4.5" stroke="var(--gold)" stroke-width="2" stroke-linecap="round"/></svg>
    <span>Rug<br>Appraisals</span>
  </div>
  <div class="service" style="top:491px;">
    <svg viewBox="0 0 28 28"><circle cx="14" cy="14" r="12.5" fill="none" stroke="var(--gold)" stroke-width="1.5"/><path d="M8 18v-4h12v4zM9.5 14v-3h9v3M7 15v4M21 15v4" fill="none" stroke="var(--gold)" stroke-width="1.4"/></svg>
    <span>Upholstery<br>cleaning, silk mohair,<br>leather, etc.</span>
  </div>
  <div class="service" style="top:540px;">
    <svg viewBox="0 0 28 28"><circle cx="14" cy="14" r="12.5" fill="none" stroke="var(--gold)" stroke-width="1.5"/><path d="M7 8h14M9 8c0 5 1 9 3 12M19 8c0 5-1 9-3 12" fill="none" stroke="var(--gold)" stroke-width="1.4"/></svg>
    <span>In-home Drapery<br>Cleaning</span>
  </div>
  <div class="service" style="top:585px;">
    <svg viewBox="0 0 28 28"><circle cx="14" cy="14" r="12.5" fill="none" stroke="var(--gold)" stroke-width="1.5"/><path d="M14 7l6 2.5v4c0 4-2.6 6.5-6 7.8-3.4-1.3-6-3.8-6-7.8v-4z" fill="none" stroke="var(--gold)" stroke-width="1.4"/><path d="M11 14l2 2 4-4" fill="none" stroke="var(--gold)" stroke-width="1.4"/></svg>
    <span>FiberGuard Fabric<br>protection for rags,<br>drapery and<br>upholstery</span>
  </div>

  <!-- centre column -->
  <div class="abs brand">
    <div class="brand-main">Regency</div>
    <div class="brand-sub">Fabric Care</div>
  </div>
  <div class="abs photo photo-cleaning" role="img" aria-label="Technician cleaning an oriental rug with a wand"></div>
  <div class="abs photo photo-living" role="img" aria-label="Cream sofa with navy cushions in a bright living room"></div>
  <div class="abs protection">PEACE OF MIND PROTECTION<br>FOR ALL YOUR PREMIUM FABRICS</div>
  <div class="abs partner"><i></i>FiberGuard</div>
  <div class="abs contact-box"></div>
  <div class="abs tagline">Expert Care. Beautiful Results.</div>
  <div class="abs phone">Ph 555 014-0277</div>
  <div class="abs contact-divider"></div>
  <div class="abs website">Website</div>
  <div class="abs qr-slot"></div>
  <div class="abs history">Since 1980 we have cleaned and protected<br>our clients rugs and furniture.</div>

  <!-- values & credentials column -->
  <div class="abs mission">Our mission<br>is to serve</div>
  <div class="rule-h" style="left:682px; top:115px; width:169px;"></div>
  <ul class="abs values">
    <li>Integrity</li>
    <li>Experience</li>
    <li>Comunication</li>
    <li>Gratitude</li>
  </ul>
  <div class="rule-h" style="left:682px; top:249px; width:169px;"></div>
  <div class="abs credentials-title">Our Credentials</div>

  <div class="credential" style="top:309px;">
    <svg viewBox="0 0 26 26"><path d="M2 14l7 8L24 3" fill="none" stroke="var(--gold)" stroke-width="4" stroke-linecap="round" stroke-linejoin="round"/></svg>
    <span>Serving clients<br>since 1980</span>
  </div>
  <div class="credential" style="top:358px;">
    <svg viewBox="0 0 26 26"><path d="M2 14l7 8L24 3" fill="none" stroke="var(--gold)" stroke-width="4" stroke-linecap="round" stroke-linejoin="round"/></svg>
    <span>Graduate of<br>Halvorsen Rug<br>Cleaning Specialist</span>
  </div>
  <div class="credential" style="top:422px;">
    <svg viewBox="0 0 26 26"><path d="M2 14l7 8L24 3" fill="none" stroke="var(--gold)" stroke-width="4" stroke-linecap="round" stroke-linejoin="round"/></svg>
    <span>ICFR: Master<br>Upholstery &amp;<br>Drapery Cleaner</span>
  </div>
  <div class="abs certificate-frame"></div>
  <div class="abs certificate" role="img" aria-label="Framed rug cleaning specialist diploma"></div>

  <!-- spec sheet -->
  <div class="abs spec-title">Tradeshow<br>Backdrop</div>
  <div class="spec-label" style="top:152px;">Size</div>
  <div class="spec-value" style="top:178px;">10ft.x7.6ft</div>
  <div class="spec-label" style="top:243px;">DPI</div>
  <div class="spec-value" style="top:266px;">300 DPI</div>
  <div class="spec-label" style="top:320px;">COLOR MODE</div>
  <div class="spec-value" style="top:344px;">CMYK</div>
  <div class="spec-note" style="top:419px;">Everything is Vectorized<br>Except images</div>
  <div class="spec-note" style="top:477px;">Images are at 300DPI</div>
  <div class="spec-note" style="top:512px;">Please share link to you<br>website and I’ll add the<br>QR code in the white BOX</div>
  <div class="swatch" style="left:888px; background:var(--gold);"></div>
  <div class="swatch" style="left:923px; background:var(--sand);"></div>
  <div class="swatch" style="left:958px; background:var(--navy);"></div>
  <div class="swatch" style="left:994px; background:#f3f1ef;"></div>

</div>
</body>
</html>
```